Need a book cover design for book titled: Rising Through the Glow--Simple Keys for the Awakening

This book describes and presents tools to connect with and activate the Lightbody that we all carry within us. It talks about the Lighbody, brief history, lightbody levels and offers exercises to bring light into the body.
I envision a design that shows a physical body changing into light /surrounded by light; a resurrected body ascending to higher dimensions of Spirit o anything comparable .

Need extra days to review

Need extra days to review

Target Market(s)

Mature audience of spiritual seekers and those on spiritual path

Requirements
Must have
• Space on backcover for book summary at top and title and author name on spine.

```html
<!DOCTYPE html>
<html lang="en">
<head>
<meta charset="utf-8">
<title>Rising Through the Glow — Book Cover Wrap</title>
<link href="https://fonts.googleapis.com/css2?family=Montserrat:wght@800&family=Cinzel:wght@400&display=swap" rel="stylesheet">
<style>
  :root {
    --page-bg: #f2f2f2;
    --space-black: #07070b;
    --space-deep: #111018;
    --nebula-magenta: #8a2a55;
    --nebula-violet: #4a3a6e;
    --nebula-teal: #3f8f8a;
    --cloud-grey: #bdb9b4;
    --cloud-warm: #a89e94;
    --glow-white: #ffffff;
    --title-white: #f4f4f4;
    --body-text: #d9d6d2;
    --rule-grey: #9a9aa0;
    --spine-grey: #c8c8c8;
    --spine-ink: #141414;
  }
  * { margin: 0; padding: 0; box-sizing: border-box; }
  html, body {
    width: 1200px;
    height: 1000px;
    overflow: hidden;
    background: var(--page-bg);
  }
  .canvas {
    position: relative;
    width: 1200px;
    height: 1000px;
  }
  .book-wrap {
    position: absolute;
    left: 65px;
    top: 125px;
    width: 1070px;
    height: 750px;
    display: flex;
    box-shadow: 0 6px 24px rgba(0,0,0,0.18);
  }

  /* ---------- Back cover ---------- */
  .back-cover {
    position: relative;
    width: 500px;
    height: 100%;
    background:
      radial-gradient(ellipse 30% 20% at 95% 90%, rgba(138,42,85,0.35), transparent 75%),
      linear-gradient(180deg, var(--space-deep), var(--space-black));
    color: var(--body-text);
    font-family: "Cinzel", serif;
    padding: 70px 48px 0;
  }
  .back-summary p {
    font-size: 12px;
    line-height: 1.6;
    text-align: center;
    margin-bottom: 26px;
  }
  .back-footer {
    position: absolute;
    left: 48px;
    right: 48px;
    bottom: 56px;
    display: flex;
    justify-content: space-between;
    align-items: flex-end;
    font-size: 9px;
    line-height: 1.5;
  }
  .back-footer .author-bio { width: 170px; }
  .back-footer .shelf-category { width: 120px; text-align: right; }

  /* ---------- Spine ---------- */
  .spine {
    position: relative;
    width: 70px;
    height: 100%;
    background: linear-gradient(90deg, #b3b3b3, var(--spine-grey) 40%, #d6d6d6);
    color: var(--spine-ink);
    display: flex;
    flex-direction: column;
    align-items: center;
    padding: 34px 0 26px;
  }
  .spine-text {
    writing-mode: vertical-rl;
    display: flex;
    flex-direction: column;
    align-items: center;
  }
  .spine-title {
    font-family: "Montserrat", sans-serif;
    font-weight: 800;
    font-size: 25px;
    letter-spacing: 1px;
    text-transform: uppercase;
    line-height: 1;
  }
  .spine-subtitle {
    font-family: "Cinzel", serif;
    font-size: 11px;
    letter-spacing: 3px;
    margin-top: 6px;
  }
  .spine-author {
    margin-top: auto;
    writing-mode: vertical-rl;
    font-family: "Cinzel", serif;
    font-size: 12px;
    letter-spacing: 1px;
    text-align: center;
    line-height: 1.3;
  }

  /* ---------- Front cover ---------- */
  .front-cover {
    position: relative;
    width: 500px;
    height: 100%;
    overflow: hidden;
    background: var(--space-black);
  }
  .cover-art {
    position: absolute;
    inset: 0;
    background:
      radial-gradient(ellipse 22% 14% at 55% 52%, rgba(63,143,138,0.35), transparent 70%),
      radial-gradient(ellipse 35% 24% at 38% 60%, rgba(138,42,85,0.55), transparent 72%),
      radial-gradient(ellipse 50% 34% at 50% 58%, rgba(74,58,110,0.45), transparent 75%),
      radial-gradient(ellipse 75% 13% at 55% 100%, var(--cloud-warm), transparent 80%),
      radial-gradient(ellipse 38% 15% at 6% 95%, var(--cloud-warm), transparent 80%),
      radial-gradient(ellipse 22% 10% at 6% 3%, var(--cloud-grey), transparent 85%),
      radial-gradient(ellipse 24% 11% at 94% 4%, var(--cloud-grey), transparent 85%),
      linear-gradient(180deg, var(--space-deep), var(--space-black) 50%, var(--space-deep));
  }
  .figure-glow {
    position: absolute;
    left: 190px;
    top: 355px;
    width: 120px;
    height: 300px;
    border-radius: 45% 45% 40% 40% / 25% 25% 60% 60%;
    background: radial-gradient(ellipse 50% 50% at 50% 40%, rgba(255,255,255,0.95), rgba(255,255,255,0.55) 55%, rgba(255,255,255,0.08) 90%);
    box-shadow: 0 0 40px 14px rgba(255,255,255,0.35);
  }
  .cover-title {
    position: absolute;
    left: 0;
    right: 0;
    top: 82px;
    text-align: center;
    font-family: "Montserrat", sans-serif;
    font-weight: 800;
    color: var(--title-white);
    text-transform: uppercase;
    line-height: 1;
  }
  .cover-title .title-lead {
    display: block;
    font-size: 32px;
    letter-spacing: 1px;
  }
  .cover-title .title-main {
    display: block;
    font-size: 66px;
    letter-spacing: 2px;
    margin-top: 8px;
  }
  .cover-rule {
    position: absolute;
    left: 45px;
    width: 410px;
    top: 205px;
    height: 1px;
    background: var(--rule-grey);
  }
  .cover-subtitle {
    position: absolute;
    left: 0;
    right: 0;
    top: 214px;
    text-align: center;
    font-family: "Cinzel", serif;
    font-size: 14px;
    letter-spacing: 2px;
    color: var(--title-white);
  }
</style>
</head>
<body>
<main class="canvas">
  <div class="book-wrap">
    <section class="back-cover">
      <div class="back-summary">
        <p>Within every one of us waits a body of pure light, patient and ready to awaken.</p>
        <p>This gentle guide explains the Lightbody, traces its brief history and maps each level of its unfolding.</p>
        <p>Step by step, simple exercises show how to draw light into every cell and feel it rise.</p>
        <p>For seekers already on the path, it offers calm, practical keys for daily spiritual growth.</p>
        <p>Open these pages and let your own inner glow lead you gently toward higher realms of Spirit.</p>
      </div>
      <div class="back-footer">
        <p class="author-bio">About the author: a lifelong teacher of light, breath and quiet inner healing.</p>
        <p class="shelf-category">Spirituality / Personal Growth</p>
      </div>
    </section>

    <section class="spine">
      <div class="spine-text">
        <span class="spine-title">Rising Through the Glow</span>
        <span class="spine-subtitle">Simple Keys for the Awakening</span>
      </div>
      <span class="spine-author">Author's<br>Name</span>
    </section>

    <section class="front-cover">
      <div class="cover-art" role="img" aria-label="Starry night sky with a violet and magenta nebula, soft grey clouds framing the top corners and the bottom edge"></div>
      <div class="figure-glow" role="img" aria-label="Glowing white silhouette of a human body rising upward, its physical outline turning into light"></div>
      <h1 class="cover-title">
        <span class="title-lead">Rising Through</span>
        <span class="title-main">the Glow</span>
      </h1>
      <div class="cover-rule"></div>
      <p class="cover-subtitle">Simple Keys for the Awakening</p>
    </section>
  </div>
</main>
</body>
</html>
```